Dravolith Business Card

I have a logo that I would like to use to design the Business Card for Dravolith Construction LLC. We are a commercial general contractor in San Antonio Texas. Id like a simple and sleek design. Message me if you have any questions. Thanks

Industry/Entity Type

Contractor

```html
<!DOCTYPE html>
<html lang="en">
<head>
<meta charset="utf-8">
<title>Dravolith Business Card</title>
<link rel="stylesheet" href="https://fonts.googleapis.com/css2?family=Lato:wght@400;700;900&display=swap">
<style>
  :root {
    --backdrop: #2e2e2e;
    --card: #ffffff;
    --brand-blue: #3467b8;
    --name-blue: #2f5fb3;
    --ink: #1e1e1e;
    --text: #333333;
    --band-dark: #1f1f1f;
  }
  * { box-sizing: border-box; margin: 0; padding: 0; }
  html, body { width: 1200px; height: 750px; overflow: hidden; }
  body {
    position: relative;
    background: var(--backdrop);
    font-family: "Lato", Arial, sans-serif;
    color: var(--text);
  }
  .card {
    position: absolute;
    top: 198px;
    height: 322px;
    background: var(--card);
    border-radius: 22px;
    overflow: hidden;
  }
  .card-front { left: 20px; width: 565px; }
  .card-back { left: 606px; width: 567px; }

  .wordmark {
    font-family: "Lato", Arial, sans-serif;
    font-weight: 900;
    color: var(--ink);
    text-transform: uppercase;
    line-height: 0.95;
    letter-spacing: -0.5px;
  }
  .card-front .wordmark {
    position: absolute;
    left: 268px;
    top: 214px;
    font-size: 27px;
  }
  .card-front .web {
    position: absolute;
    left: 269px;
    top: 272px;
    font-size: 16px;
    letter-spacing: 1.6px;
    color: var(--text);
  }

  .holder {
    position: absolute;
    left: 34px;
    top: 60px;
  }
  .holder-name {
    font-size: 20px;
    font-weight: 400;
    color: var(--name-blue);
  }
  .holder-role {
    font-size: 13px;
    margin-top: 4px;
    color: var(--ink);
  }
  .contacts {
    position: absolute;
    left: 34px;
    top: 136px;
    list-style: none;
    font-size: 12px;
  }
  .contacts li {
    display: flex;
    align-items: center;
    height: 17.7px;
  }
  .contacts svg {
    width: 10px;
    height: 10px;
    margin-right: 9px;
    fill: var(--brand-blue);
  }
  .address {
    position: absolute;
    left: 34px;
    top: 225px;
    font-size: 12px;
    font-style: normal;
    line-height: 17px;
  }
  .card-back .wordmark {
    position: absolute;
    right: 36px;
    top: 214px;
    font-size: 21px;
    text-align: left;
  }
  .band {
    position: absolute;
    left: 0;
    top: 0;
    width: 567px;
    height: 322px;
  }
</style>
</head>
<body>

<section class="card card-front" aria-label="Card front">
  <div class="wordmark">Dravolith<br>Construction LLC</div>
  <div class="web">www.dravolith.com</div>
</section>

<section class="card card-back" aria-label="Card back">
  <svg class="band" viewBox="0 0 567 322" aria-hidden="true">
    <polygon points="0,298 290,298 282,309 0,309" fill="var(--band-dark)"/>
    <polygon points="0,313 288,313 304,289 567,289 567,322 0,322" fill="var(--brand-blue)"/>
  </svg>

  <div class="holder">
    <h1 class="holder-name">Daniel Reyes</h1>
    <p class="holder-role">Occupation</p>
  </div>

  <ul class="contacts">
    <li>
      <svg viewBox="0 0 10 10"><path d="M2 0.5 L3.6 2.6 L2.8 3.6 Q4 6 6.4 7.2 L7.4 6.4 L9.5 8 L8.4 9.5 Q3.5 9 0.5 1.6 Z"/></svg>
      (210) 555 0148
    </li>
    <li>
      <svg viewBox="0 0 10 10"><rect x="2.5" y="0.5" width="5" height="3"/><rect x="0.5" y="3.5" width="9" height="4" rx="0.8"/><rect x="2.5" y="6.5" width="5" height="3"/></svg>
      210-555-0192
    </li>
    <li>
      <svg viewBox="0 0 10 10"><path d="M0.5 2 H9.5 V8.5 H0.5 Z M0.5 2 L5 5.5 L9.5 2" stroke="#fff" stroke-width="0.8"/></svg>
      danielr@dravolith.com
    </li>
    <li>
      <svg viewBox="0 0 10 10"><circle cx="5" cy="5" r="4.6"/><path d="M2.5 3 Q4 4 3.5 5.5 Q5 6 4.5 8 M6 1.5 Q6.5 3 8 3.5" stroke="#fff" stroke-width="0.8" fill="none"/></svg>
      www.dravolith.com
    </li>
  </ul>

  <address class="address">
    Ground Floor 12 Halvern Circuit<br>
    Halvern Business Park
  </address>

  <div class="wordmark">Dravolith<br>Construction LLC</div>
</section>

</body>
</html>
```